Tech Startup Needs Business Card Design

I am looking for an eye catching business card design for our new company, Blue Kettle. We are a place for business owners and contractors to share their experiences with their customers and check their current customers. Our website, www.blue-kettle.example, may be able to offer some guidance as to the design.

Industry/Entity Type

Business

Contact Information for Business Card

Tom Varrowby
888-555-0147
Tom@blue-kettle.example
www.blue-kettle.example

```html
<!DOCTYPE html>
<html lang="en">
<head>
<meta charset="utf-8">
<title>Blue Kettle – Business Card</title>
<link rel="stylesheet" href="https://fonts.googleapis.com/css2?family=Ubuntu:wght@400;500;700&display=swap">
<style>
  :root {
    --brand-red: #ec2129;
    --ink: #1c1c1c;
    --card-white: #ffffff;
    --backdrop: #ece6da;
  }
  * { margin: 0; padding: 0; box-sizing: border-box; }
  html, body {
    width: 1189px;
    height: 1200px;
    overflow: hidden;
    background: var(--backdrop);
    font-family: "Ubuntu", sans-serif;
  }
  .card {
    position: absolute;
    left: 171px;
    width: 856px;
    height: 487px;
    border-radius: 24px;
    overflow: hidden;
  }
  .card-front {
    top: 68px;
    background: var(--brand-red);
    display: flex;
    align-items: center;
    justify-content: center;
  }
  .wordmark-front {
    color: var(--card-white);
    font-weight: 500;
    font-size: 112px;
    letter-spacing: 1px;
    line-height: 1;
  }
  .card-back {
    top: 627px;
    background: var(--card-white);
  }
  .brand-block {
    position: absolute;
    left: 0;
    width: 402px;
    top: 0;
    height: 487px;
    display: flex;
    align-items: center;
    justify-content: center;
    gap: 14px;
  }
  .brand-dot {
    width: 26px;
    height: 26px;
    border-radius: 50%;
    background: var(--brand-red);
  }
  .wordmark-back {
    color: var(--brand-red);
    font-weight: 500;
    font-size: 44px;
    line-height: 1;
  }
  .divider {
    position: absolute;
    left: 402px;
    top: 125px;
    width: 1.5px;
    height: 244px;
    background: var(--ink);
  }
  .contact {
    position: absolute;
    left: 478px;
    top: 122px;
    color: var(--ink);
  }
  .contact-name {
    color: var(--brand-red);
    font-weight: 700;
    font-size: 29px;
    line-height: 1;
    margin-bottom: 39px;
  }
  .contact-address {
    font-size: 23px;
    line-height: 30px;
    margin-bottom: 12px;
  }
  .contact-line {
    display: flex;
    align-items: center;
    gap: 8px;
    font-size: 23px;
    line-height: 30px;
  }
  .contact-icon {
    width: 27px;
    height: 25px;
    flex: none;
  }
  .contact-web {
    color: var(--brand-red);
    font-size: 23px;
    line-height: 30px;
    margin-top: 12px;
  }
</style>
</head>
<body>
  <section class="card card-front">
    <span class="wordmark-front">Blue Kettle</span>
  </section>

  <section class="card card-back">
    <div class="brand-block">
      <span class="brand-dot"></span>
      <span class="wordmark-back">Blue Kettle</span>
    </div>
    <div class="divider"></div>
    <div class="contact">
      <p class="contact-name">Tom Varrowby</p>
      <p class="contact-address">your address,2nd street<br>Harlow Ridge East. USA</p>
      <p class="contact-line">
        <svg class="contact-icon" viewBox="0 0 27 25" aria-hidden="true">
          <rect width="27" height="25" rx="3" fill="var(--brand-red)"/>
          <path d="M9 5 l3 0 l1.5 4 l-2 1.5 q1.5 3.5 4 5 l1.5 -2 l4 1.5 l0 3 q-8 1 -12 -13 z" fill="#fff"/>
        </svg>
        888-555-0147
      </p>
      <p class="contact-line">
        <svg class="contact-icon" viewBox="0 0 27 25" aria-hidden="true">
          <rect width="27" height="25" rx="3" fill="var(--brand-red)"/>
          <rect x="5" y="7" width="17" height="11" fill="none" stroke="#fff" stroke-width="1.6"/>
          <path d="M5 7 l8.5 6.5 l8.5 -6.5" fill="none" stroke="#fff" stroke-width="1.6"/>
        </svg>
        Tom@blue-kettle.example
      </p>
      <p class="contact-web">blue-kettle.example</p>
    </div>
  </section>
</body>
</html>
```